Orvek Electric Construction Power Runs Deep!

We have an up coming meeting with a developer and general contractor. This card must bring out the best in my business. My business is an up and coming MDBE certified electrical contactor. I need a very powerful card to represent me business that we be bold and represent what I am about. POWER RUNS DEEP!

Target Market(s)

General Contractors, developers and property owners

Industry/Entity Type

Electrical

Contact Information for Business Card

great card that really brings out my bussiness

Colors
0355a3
3276b5
0393ce
34a6d7

Requirements
Must have
• Great design
Nice to have
• very different and noticeable card
Should not have
• open to anything

```html
<!DOCTYPE html>
<html lang="en">
<head>
<meta charset="utf-8">
<title>Orvek Electric Construction – Business Card</title>
<link rel="stylesheet" href="https://fonts.googleapis.com/css2?family=Quicksand:wght@400;500;700&family=Arimo:wght@400&display=swap">
<style>
  :root {
    --navy: #0355a3;
    --blue: #3276b5;
    --sky: #0393ce;
    --light-sky: #34a6d7;
    --paper: #f4f5f6;
    --backdrop: #e9ebee;
    --white: #ffffff;
  }
  html, body {
    margin: 0;
    width: 1200px;
    height: 800px;
    overflow: hidden;
    background: var(--backdrop);
  }
  .canvas {
    position: relative;
    width: 1200px;
    height: 800px;
  }
  .business-card {
    position: absolute;
    left: 75px;
    top: 100px;
    width: 1050px;
    height: 600px;
    background: var(--paper);
    box-shadow: 0 6px 24px rgba(20, 40, 70, 0.12);
    overflow: hidden;
  }
  .card-wave {
    position: absolute;
    inset: 0;
  }
  .brand {
    position: absolute;
    left: 220px;
    top: 110px;
    width: 420px;
    text-align: center;
  }
  .brand-dot {
    width: 58px;
    height: 58px;
    margin: 0 auto 26px;
    border-radius: 50%;
    background: var(--navy);
  }
  .brand-name {
    margin: 0;
    font-family: "Arimo", Arial, sans-serif;
    font-weight: 400;
    font-size: 36px;
    color: var(--sky);
    letter-spacing: 0.2px;
  }
  .holder {
    position: absolute;
    left: 42px;
    bottom: 38px;
    color: var(--white);
    font-family: "Quicksand", sans-serif;
  }
  .holder-name {
    margin: 0;
    font-size: 46px;
    font-weight: 700;
    line-height: 1;
  }
  .holder-title {
    margin: 4px 0 0 4px;
    font-size: 22px;
    font-weight: 500;
  }
  .contact-list {
    position: absolute;
    left: 610px;
    top: 330px;
    margin: 0;
    padding: 0;
    list-style: none;
    color: var(--white);
    font-family: "Quicksand", sans-serif;
    font-size: 25px;
    font-weight: 400;
    line-height: 1.3;
  }
  .contact-item {
    display: flex;
    align-items: flex-start;
    gap: 14px;
    margin-bottom: 8px;
  }
  .contact-icon {
    flex: 0 0 24px;
    width: 24px;
    height: 24px;
    margin-top: 5px;
    fill: var(--white);
  }
</style>
</head>
<body>
<main class="canvas">
  <section class="business-card" aria-label="Orvek Electric Construction business card">
    <svg class="card-wave" viewBox="0 0 1050 600" preserveAspectRatio="none" aria-hidden="true">
      <defs>
        <linearGradient id="waveFill" x1="0" y1="1" x2="1" y2="0">
          <stop offset="0" stop-color="var(--navy)"/>
          <stop offset="0.6" stop-color="var(--blue)"/>
          <stop offset="1" stop-color="var(--blue)"/>
        </linearGradient>
      </defs>
      <path d="M0,470 C260,370 700,380 880,0 L1050,0 L1050,600 L0,600 Z" fill="url(#waveFill)"/>
      <path d="M0,448 C250,350 680,355 852,0 L858,0 C690,368 258,362 0,458 Z" fill="var(--navy)"/>
    </svg>

    <div class="brand">
      <div class="brand-dot"></div>
      <h1 class="brand-name">Orvek Electric Construction</h1>
    </div>

    <ul class="contact-list">
      <li class="contact-item">
        <svg class="contact-icon" viewBox="0 0 24 24" aria-hidden="true"><path d="M6.6 10.8a15.1 15.1 0 0 0 6.6 6.6l2.2-2.2a1 1 0 0 1 1-.25 11.4 11.4 0 0 0 3.6.57 1 1 0 0 1 1 1V20a1 1 0 0 1-1 1A17 17 0 0 1 3 4a1 1 0 0 1 1-1h3.5a1 1 0 0 1 1 1c0 1.25.2 2.45.57 3.57a1 1 0 0 1-.25 1z"/></svg>
        <span>+61 400 555 017</span>
      </li>
      <li class="contact-item">
        <svg class="contact-icon" viewBox="0 0 24 24" aria-hidden="true"><path d="M2 5h20v14H2z M3.5 6.5 12 13l8.5-6.5" fill="none" stroke="#fff" stroke-width="1.8"/></svg>
        <span>hello@orvekelectric.com.au</span>
      </li>
      <li class="contact-item">
        <svg class="contact-icon" viewBox="0 0 24 24" aria-hidden="true"><path d="M12 3 2 12h3v9h5v-6h4v6h5v-9h3z"/></svg>
        <span>42 Fenwick Lane Melbourne VIC<br>3000 Australia</span>
      </li>
    </ul>

    <div class="holder">
      <p class="holder-name">Daniel Harrow</p>
      <p class="holder-title">Director</p>
    </div>
  </section>
</main>
</body>
</html>
```